Book Cover design - Education & Research

We need a design of the book cover for a book written in an education sector. It has been written by a professor with target audience being other professors, lecturers, PhD students etc. The book is about Singapore's development as a country (from third world to economical leader) with high emphasis on it's education sector. It explores many education concepts that could set an example for other countries.
We would like the design to be serious, modern, representing innovation, progress in the educations space. The colours will be mainly red and white representing the country's flag. Probably white background with red additions. The design will consist of three parts:
1) Front cover (the most important where the designer should put most effort in). At the top will be name of the author: Zofia Kradecka, below name of the book: "Odlegle Sciezki Nauczania" with smaller subtitle below: "Zielone Mosty Pomiedzy Szkolami Zielone Mosty Pomiedzy Szkolami"
2) Back cover (very simple with majority of the space put for text, reviews etc.)
3) Second page already inside the book (less important, just a simple black and white design in this part)
We welcome any creative designs from your part, but for reference below is an idea of how we would like it to look like. I would recommend for the designers to do two designs. One according to the below instructions and another with your own idea how to go about it. Please do keep in mind that we can't use proprietary Singapore icons like quorvex or exact design of Singapore flag, so please don't use these.
Our idea:
- The front page to have cityscape with silhouettes of Singapore iconic buildings (Coral Hill Towers, Halvern Wheel, Lumen Craft Gallery, Corvanta, Terraces of Wrenfield, Sky scrappers)
- A red and white ribbon starting at the front and then going through the spine of the book to the back cover.
NOTE:
- We would like to see more designs with your own creativity and other colors, not only red and white
Education sector, Universities, Professors

```html
<!DOCTYPE html>
<html lang="pl">
<head>
<meta charset="utf-8">
<title>Odlegle Sciezki Nauczania – tylna okladka</title>
<link rel="stylesheet" href="https://fonts.googleapis.com/css2?family=Source+Sans+3:ital,wght@0,300;0,400;1,400;1,500&display=swap">
<style>
  :root {
    --sky: #d1eaf6;
    --flag-red: #e30613;
    --ink: #111111;
    --ink-soft: #2b2b2b;
    --paper: #ffffff;
    --trim: #1a1a1a;
    --city-pink: #e8c3cf;
    --city-lilac: #d9cde3;
    --city-blue: #c9d6ee;
    --ground: #b9a9bd;
  }
  * { margin: 0; padding: 0; box-sizing: border-box; }
  html, body {
    width: 856px; height: 1200px; overflow: hidden;
    background: var(--paper);
  }
  .back-cover {
    position: relative;
    width: 856px; height: 1200px;
    background: var(--paper);
    font-family: "Source Sans 3", "Myriad Pro", sans-serif;
    color: var(--ink);
  }
  .reviews-panel {
    position: absolute;
    left: 19px; top: 18px;
    width: 820px; height: 680px;
    background: var(--sky);
  }
  .review {
    position: absolute;
    left: 92px; width: 620px;
  }
  .review-quote {
    text-align: center;
    font-size: 19.5px;
    line-height: 35px;
  }
  .review--featured .review-quote {
    font-style: italic;
    font-weight: 500;
    color: var(--ink);
  }
  .review--plain .review-quote {
    font-weight: 300;
    color: var(--ink-soft);
  }
  .review-source {
    text-align: right;
    font-size: 21px;
    font-weight: 400;
    margin-top: 12px;
    color: var(--ink);
  }
  .review--one { top: 55px; }
  .review--two { top: 337px; }
  .review--three { top: 523px; }
  .ribbon-band {
    position: absolute;
    left: 0; top: 698px;
    width: 856px; height: 116px;
    background: var(--flag-red);
  }
  .skyline {
    position: absolute;
    left: 74px; top: 838px;
    width: 730px; height: 330px;
    background:
      radial-gradient(ellipse at 28% 70%, rgba(201,214,238,0.9), transparent 55%),
      radial-gradient(ellipse at 65% 55%, rgba(232,195,207,0.9), transparent 60%),
      linear-gradient(180deg, var(--paper) 0%, var(--city-lilac) 45%, var(--city-pink) 100%);
  }
  .ground-line {
    position: absolute;
    left: 5px; top: 1160px;
    width: 846px; height: 14px;
    background: linear-gradient(180deg, #a9a9a9 0%, var(--ground) 50%, #d8c4d3 100%);
  }
  .trim-frame {
    position: absolute;
    left: 19px; top: 18px;
    width: 821px; height: 1164px;
    border: 1px solid var(--trim);
    pointer-events: none;
  }
</style>
</head>
<body>
  <main class="back-cover">
    <section class="reviews-panel"></section>

    <article class="review review--featured review--one">
      <p class="review-quote">"Zielone Mosty Pomiedzy Szkolami Zielone Mosty Pomiedzy Szkolami Zielone Mosty Pomiedzy Szkolami Zielone Mosty Pomiedzy Szkolami Zielone Mosty Pomiedzy Szkolami Zielone Mosty Pomiedzy Szkolami Zielone Mosty Pomiedzy Szkolami Zielone Mosty Pomiedzy Szkolami Zielone Mosty Pomiedzy Szkolami Zielone Mosty Pomiedzy Szkolami Zielone Mosty Pomiedzy Szkolami"</p>
      <p class="review-source">-Zielone Mosty Pomiedzy</p>
    </article>

    <article class="review review--plain review--two">
      <p class="review-quote">"Zielone Mosty Pomiedzy Szkolami Zielone Mosty Pomiedzy Szkolami Zielone Mosty Pomiedzy Szkolami Zielone Mosty Pomiedzy Szkolami Zielone Mosty "</p>
      <p class="review-source">-Zielone Mosty Pomiedzy</p>
    </article>

    <article class="review review--plain review--three">
      <p class="review-quote">"Zielone Mosty Pomiedzy Szkolami Zielone Mosty Pomiedzy Szkolami Zielone Mosty Pomiedzy Szkolami Zielone Mosty Pomiedzy Szkolami Zielone Mosty "</p>
      <p class="review-source">-Zielone Mosty Pomiedzy</p>
    </article>

    <div class="ribbon-band"></div>

    <div class="skyline" role="img" aria-label="Ilustracja panoramy miasta w pastelowych różach i błękitach: wieżowce, Coral Hill Towers, Terraces of Wrenfield, Corvanta, Lumen Craft Gallery i Halvern Wheel"></div>
    <div class="ground-line"></div>

    <div class="trim-frame"></div>
  </main>
</body>
</html>
```